TRIVAN 2026 Flyer for Conference

TRIVAN needs a design for a 1-page flyer that we will hand out at an upcoming event & then later post online as a pdf. There are 3 elements which need to be on the flyer:

1) A logo. This should be prominent on the design (e.g., in the middle). The flyer should use the colors that are in that logo (e.g., for accents, design elements, and/or text; not all of these have to be used):
Dark blue: #185577
Med blue: #327C9A
Teal: #4EB1C2
Light Teal: #9EDBE6

2) The conference theme -- Forests of Wonder: Climbing toward Research Fluency -- should be at the flyer's top.

3) Finally, these six tracks should be listed below the theme and the logo (it's font size should be at least a couple sizes smaller than the size used for the theme):
- Pearls of Pedagogy: Teaching Techniques that Work
- The Depth Gauge: Measuring Instructional Impact
- Techtonic Shifts: Innovation and Educational Technology
- Captain's Log: Navigating Leadership in Library Instruction
- Swimming Together: Collaborating with Others
- The Bermuda Triangle: Exploring (Seemingly) Eternal Challenges

Font styles to use
Sans Serif

Colors
0094D4
00A9DD
6FCCEA
C7EBF8
E9F6FB

Requirements
Must have
• The 3 elements listed in the description: 1) the logo, 2) the text of the theme and 3) the text for the tracks.

```html
<!DOCTYPE html>
<html lang="en">
<head>
<meta charset="utf-8">
<title>TRIVAN 2026 – Forests of Wonder</title>
<link rel="stylesheet" href="https://fonts.googleapis.com/css2?family=Montserrat:ital,wght@0,400;0,700;0,800;1,700&display=swap">
<style>
  :root {
    --dark-blue: #185577;
    --med-blue: #327C9A;
    --teal: #4EB1C2;
    --light-teal: #9EDBE6;
    --sea-top: #2a8fcf;
    --sea-mid: #12508a;
    --sea-deep: #0a2a4a;
    --title-fill: #1b6aa9;
    --white: #ffffff;
    --ink-shadow: #0b2a44;
  }
  * { margin: 0; padding: 0; box-sizing: border-box; }
  html, body { width: 901px; height: 1200px; overflow: hidden; background: #d4d5d5; }
  .flyer {
    position: relative;
    width: 901px;
    height: 1200px;
    overflow: hidden;
    font-family: "Montserrat", sans-serif;
    color: var(--white);
  }
  .backdrop {
    position: absolute; inset: 0;
    background:
      radial-gradient(ellipse at 50% 0%, rgba(190,235,255,0.55) 0%, rgba(190,235,255,0) 45%),
      linear-gradient(180deg, var(--sea-top) 0%, #1668a6 30%, var(--sea-mid) 55%, #113f66 75%, var(--sea-deep) 100%);
  }
  .brand {
    position: absolute; top: 58px; left: 0; width: 100%;
    display: flex; justify-content: center; align-items: center; gap: 12px;
  }
  .brand-dot { width: 22px; height: 22px; border-radius: 50%; background: var(--light-teal); }
  .brand-name {
    font-weight: 800; font-size: 46px; letter-spacing: 2px; color: var(--dark-blue);
  }
  .presents {
    position: absolute; top: 152px; left: 0; width: 100%;
    text-align: center; font-weight: 800; font-size: 21px; line-height: 28px;
    text-shadow: 2px 2px 0 var(--ink-shadow);
  }
  .theme-title {
    position: absolute; top: 222px; left: 0; width: 100%;
    text-align: center; font-weight: 800; text-transform: uppercase; line-height: 1;
  }
  .theme-line1 {
    display: block; font-size: 96px; color: var(--light-teal);
    text-shadow: 4px 4px 0 var(--ink-shadow);
  }
  .theme-line2 {
    display: block; margin-top: 8px; font-size: 104px; letter-spacing: 2px;
    color: var(--title-fill);
    text-shadow:
      2px 0 0 var(--white), -2px 0 0 var(--white),
      0 2px 0 var(--white), 0 -2px 0 var(--white),
      1.5px 1.5px 0 var(--white), -1.5px -1.5px 0 var(--white),
      1.5px -1.5px 0 var(--white), -1.5px 1.5px 0 var(--white);
  }
  .theme-sub {
    position: absolute; top: 428px; left: 0; width: 100%;
    text-align: center; font-weight: 700; font-style: italic; font-size: 32px;
    text-shadow: 3px 3px 0 var(--ink-shadow);
  }
  .hero-art {
    position: absolute; left: 107px; top: 478px; width: 640px; height: 350px;
    border-radius: 40% 40% 12px 12px;
    background: radial-gradient(ellipse at 50% 40%, #e76a5a 0%, #4f9fd0 45%, #dfe8ef 78%, rgba(223,232,239,0) 100%);
  }
  .tracks {
    position: absolute; top: 850px; left: 29px; width: 850px;
    display: grid; grid-template-columns: 442px 408px; row-gap: 16px;
    list-style: none;
  }
  .track { display: flex; gap: 14px; align-items: flex-start; }
  .track-tick { flex: none; width: 18px; height: 18px; margin-top: 4px; }
  .track-name {
    display: block; font-weight: 700; font-size: 21px; line-height: 26px;
    color: var(--light-teal); text-transform: uppercase;
  }
  .track-desc { display: block; max-width: 380px; font-weight: 400; font-size: 19.5px; line-height: 26px; letter-spacing: 0.4px; }
  .site {
    position: absolute; top: 1123px; left: 0; width: 100%;
    text-align: center; font-size: 17px; letter-spacing: 2.4px;
  }
</style>
</head>
<body>
<main class="flyer">
  <div class="backdrop" role="img" aria-label="Underwater ocean scene with sunlight rays and a rocky reef floor"></div>

  <div class="brand">
    <span class="brand-dot"></span>
    <span class="brand-name">TRIVAN</span>
  </div>

  <p class="presents">TRIVAN 2026<br>PRESENTS</p>

  <h1 class="theme-title">
    <span class="theme-line1">Forests of</span>
    <span class="theme-line2">Wonder</span>
  </h1>
  <p class="theme-sub">Climbing toward Research Fluency</p>

  <div class="hero-art" role="img" aria-label="Open book with a colourful coral reef growing out of its pages"></div>

  <ul class="tracks">
    <li class="track">
      <svg class="track-tick" viewBox="0 0 18 18"><circle cx="9" cy="9" r="7.5" fill="none" stroke="#fff" stroke-width="1.6"/><path d="M5.5 9.2l2.4 2.4 5-5.2" fill="none" stroke="#fff" stroke-width="1.8"/></svg>
      <div><span class="track-name">Pearls of Pedagogy</span><span class="track-desc">Teaching Techniques that Work</span></div>
    </li>
    <li class="track">
      <svg class="track-tick" viewBox="0 0 18 18"><circle cx="9" cy="9" r="7.5" fill="none" stroke="#fff" stroke-width="1.6"/><path d="M5.5 9.2l2.4 2.4 5-5.2" fill="none" stroke="#fff" stroke-width="1.8"/></svg>
      <div><span class="track-name">Swimming Together</span><span class="track-desc">Collaborating with Others</span></div>
    </li>
    <li class="track">
      <svg class="track-tick" viewBox="0 0 18 18"><circle cx="9" cy="9" r="7.5" fill="none" stroke="#fff" stroke-width="1.6"/><path d="M5.5 9.2l2.4 2.4 5-5.2" fill="none" stroke="#fff" stroke-width="1.8"/></svg>
      <div><span class="track-name">Techtonic Shifts</span><span class="track-desc">Innovation and Educational Technology</span></div>
    </li>
    <li class="track">
      <svg class="track-tick" viewBox="0 0 18 18"><circle cx="9" cy="9" r="7.5" fill="none" stroke="#fff" stroke-width="1.6"/><path d="M5.5 9.2l2.4 2.4 5-5.2" fill="none" stroke="#fff" stroke-width="1.8"/></svg>
      <div><span class="track-name">Captain's Log</span><span class="track-desc">Navigating Leadership in Library Instruction</span></div>
    </li>
    <li class="track">
      <svg class="track-tick" viewBox="0 0 18 18"><circle cx="9" cy="9" r="7.5" fill="none" stroke="#fff" stroke-width="1.6"/><path d="M5.5 9.2l2.4 2.4 5-5.2" fill="none" stroke="#fff" stroke-width="1.8"/></svg>
      <div><span class="track-name">The Bermuda Triangle</span><span class="track-desc">Exploring (Seemingly) Eternal Challenges</span></div>
    </li>
    <li class="track">
      <svg class="track-tick" viewBox="0 0 18 18"><circle cx="9" cy="9" r="7.5" fill="none" stroke="#fff" stroke-width="1.6"/><path d="M5.5 9.2l2.4 2.4 5-5.2" fill="none" stroke="#fff" stroke-width="1.8"/></svg>
      <div><span class="track-name">The Depth Gauge</span><span class="track-desc">Measuring Instructional Impact</span></div>
    </li>
  </ul>

  <p class="site">www.trivanconference.org</p>
</main>
</body>
</html>
```